Olive Oil Label Needs Graphic Designs

We need two sister label designs for 500ml bottles for our new brand "Casa Lumen". Casa Lumen is a high-end olive oil from Baeza, Spain which will be sold in the US. The oil will be produced from both Arbequina olives and Picual olives. Therefore, envisioning the same design just a different color scheme for the different labels.
The label should have the following characteristics; clean and simple, stand-out from mainstream labels, be eye-catching, give perception of high-end / high-quality.
Our current thinking of what we want (but please let your creative juices flow); lighter background, to be more eye catching, graphics of and olive, a olive branch or olive tree.
Text which should appear on the label are (not necessarily in this order);
Casa Lumen
Extra Virgin Olive Oil
Family Reserve
Arbequina (One design)
Picual (Second design)
The label should be about 3 inches wide and 5.5 inches in height.

```html
<!DOCTYPE html>
<html lang="en">
<head>
<meta charset="utf-8">
<title>Casa Lumen Olive Oil Labels</title>
<link rel="stylesheet" href="https://fonts.googleapis.com/css2?family=Dosis:wght@300;400;500;700&display=swap">
<style>
  :root{
    --page:#ffffff;
    --charcoal:#343537;
    --paper:#f6f6f4;
    --olive:#a3a43a;
    --olive-soft:#b3b454;
    --navy:#283241;
    --ink:#3a3b3e;
    --cream:#f1efe9;
    --muted:#c9c9c4;
    --rule-olive:#9e9f3c;
  }
  *{box-sizing:border-box;margin:0;padding:0}
  html,body{width:1200px;height:1200px;overflow:hidden;background:var(--page)}
  body{font-family:"Dosis",sans-serif;position:relative}

  .label{position:absolute;top:200px;width:340px;height:800px;overflow:hidden}
  .label--arbequina{left:40px;background:var(--charcoal);color:var(--cream)}
  .label--picual{left:430px;background:var(--paper);color:var(--ink)}
  .label--nutrition{left:820px;background:var(--charcoal);color:var(--cream)}

  .descriptor{position:absolute;left:24px;top:58px;font-weight:300;font-size:44px;line-height:58px;letter-spacing:-0.5px;text-transform:uppercase}
  .descriptor-rule{position:absolute;left:24px;top:196px;width:118px;height:5px;border-top:1.5px solid;border-bottom:1.5px solid}
  .label--arbequina .descriptor-rule{color:var(--rule-olive)}
  .label--picual .descriptor-rule{color:var(--navy)}

  .brand{position:absolute;left:22px;top:224px;font-weight:700;font-size:80px;line-height:82px;letter-spacing:-1px;text-transform:uppercase;white-space:nowrap;z-index:3}
  .label--arbequina .brand{color:var(--cream)}
  .label--picual .brand{color:var(--ink)}

  .olive-art{position:absolute;left:262px;top:396px;width:78px;height:200px;border-radius:39px 0 0 39px;z-index:2}
  .label--arbequina .olive-art{background:linear-gradient(180deg,#6f7f45 0%,#a7a83a 60%,#c2c04a 100%)}
  .label--picual .olive-art{background:linear-gradient(180deg,#7f8a55 0%,#3b4555 60%,#283241 100%)}

  .variety-band{position:absolute;left:0;right:0;top:476px;height:74px;display:flex;align-items:center;padding-left:22px;font-weight:500;font-size:44px;text-transform:uppercase;z-index:1}
  .label--arbequina .variety-band{background:var(--olive);color:var(--cream)}
  .label--picual .variety-band{background:var(--navy);color:var(--cream)}

  .reserve{position:absolute;left:70px;width:200px;top:610px;height:68px;display:flex;align-items:center;justify-content:center;font-weight:300;font-size:29px;text-transform:uppercase;letter-spacing:-0.3px;white-space:nowrap}
  .reserve::before,.reserve::after{content:"";position:absolute;left:0;right:0;height:4px;border-top:1px solid;border-bottom:1px solid;opacity:.7}
  .reserve::before{top:0}
  .reserve::after{bottom:0}
  .label--arbequina .reserve{color:var(--muted)}

  .volume{position:absolute;left:0;right:0;top:740px;text-align:center;font-weight:500;font-size:34px}

  .nf-title{position:absolute;left:22px;top:60px;font-weight:500;font-size:42px;text-transform:uppercase;letter-spacing:-0.5px;white-space:nowrap}
  .nf-serving{position:absolute;left:22px;top:118px;font-weight:300;font-size:21px;line-height:29px}
  .nf-rule{position:absolute;left:22px;right:12px;height:4px;border-top:1px solid #77787a;border-bottom:1px solid #77787a}
  .nf-amount{position:absolute;left:22px;top:200px;font-weight:300;font-size:26px}
  .nf-calories{position:absolute;left:22px;top:240px;font-weight:300;font-size:21px;line-height:29px}
  .nf-panel{position:absolute;left:2px;right:10px;top:313px;height:292px;background:var(--olive-soft);padding:14px 18px 0 20px;font-weight:300;font-size:19px;line-height:28.5px}
  .nf-row{display:flex;align-items:baseline;white-space:nowrap}
  .nf-row .dots{flex:1;border-bottom:1px dotted var(--cream);margin:0 2px;transform:translateY(-5px)}
  .nf-row.indent{padding-left:16px}
  .nf-note{position:absolute;left:22px;right:12px;font-weight:300;font-size:19px;line-height:27px}
</style>
</head>
<body>

  <section class="label label--arbequina" aria-label="Arbequina front label">
    <p class="descriptor">Extra Virgin<br>Olive Oil</p>
    <div class="descriptor-rule"></div>
    <h1 class="brand">Casa<br>Lumen</h1>
    <div class="olive-art" role="img" aria-label="Illustration of green olives on a leafy olive branch"></div>
    <div class="variety-band">Arbequina</div>
    <p class="reserve">Family Reserve</p>
    <p class="volume">500ml</p>
  </section>

  <section class="label label--picual" aria-label="Picual front label">
    <p class="descriptor">Extra Virgin<br>Olive Oil</p>
    <div class="descriptor-rule"></div>
    <h1 class="brand">Casa<br>Lumen</h1>
    <div class="olive-art" role="img" aria-label="Illustration of dark olives on a leafy olive branch"></div>
    <div class="variety-band">Picual</div>
    <p class="reserve">Family Reserve</p>
    <p class="volume">500ml</p>
  </section>

  <section class="label label--nutrition" aria-label="Nutrition facts back label">
    <h2 class="nf-title">Nutrition Facts</h2>
    <p class="nf-serving">Serving Size 1 Tbsp. (15ml)<br>Serving Per Container ~33</p>
    <div class="nf-rule" style="top:186px"></div>
    <p class="nf-amount">Amount per serving</p>
    <p class="nf-calories">Calories 120<br>Calories from Fat 120</p>
    <div class="nf-panel">
      <div class="nf-row">% Daily Value *</div>
      <div class="nf-row">Total Fat 14g<span class="dots"></span>22%</div>
      <div class="nf-row indent">Saturated Fat 2g<span class="dots"></span>10%</div>
      <div class="nf-row indent">Trans Fat 0 gr.</div>
      <div class="nf-row">Cholesterol 0 mg<span class="dots"></span>0%</div>
      <div class="nf-row">Sodium 0 g<span class="dots"></span>0%</div>
      <div class="nf-row">Total Carbohydrate 0 g<span class="dots"></span>0%</div>
      <div class="nf-row indent">Sugar 0 g</div>
      <div class="nf-row">Protein 0 g</div>
    </div>
    <p class="nf-note" style="top:622px">Not a significant source of dietary fiber, Vitamin A, Vitamin C, Calcium or Iron.</p>
    <p class="nf-note" style="top:708px">*Percent Daily Values are based on a 2,000 calorie diet.</p>
  </section>

</body>
</html>
```